Unique Business Card Design

Unique Business Card design for our orthotic and prosthetic company. Our logo is on our website, color is light blue. Unique shape (artificial leg shaped, vertical, etc..) preferred. Logo, business name, individual name and basic demographics needed.

Industry/Entity Type

Business

Contact Information for Business Card

Logo, Industry, Phone # Logo, "Prosthetic & Orthotic Services" Place to add individual name and contact info

Colors
cee9f5

Requirements
Must have
• The icon must be there, placement of "Prosthetic & Orthotic Services" can be moved
Nice to have
• Like the mix of light blue, and a little darker blue. One design included the icons from my website which was a nice touch

```html
<!DOCTYPE html>
<html lang="en">
<head>
<meta charset="utf-8">
<title>Limbwell Inc. Business Card</title>
<link rel="stylesheet" href="https://fonts.googleapis.com/css2?family=Open+Sans:wght@400;600&family=Tinos:ital@1&display=swap">
<style>
  :root {
    --backdrop: #e9edf0;
    --card: #0c3446;
    --card-edge: #0a2c3b;
    --ink: #ffffff;
    --brand-light: #cee9f5;
  }
  * { margin: 0; padding: 0; box-sizing: border-box; }
  html, body { width: 1200px; height: 902px; overflow: hidden; background: var(--backdrop); }
  body { display: flex; align-items: center; justify-content: center; font-family: "Open Sans", Arial, sans-serif; }

  .business-card {
    position: relative;
    width: 1000px;
    height: 572px;
    border-radius: 34px;
    background: linear-gradient(135deg, #124257 0%, var(--card) 45%, var(--card-edge) 100%);
    color: var(--ink);
    box-shadow: 0 18px 40px rgba(10, 40, 55, 0.25);
  }

  /* Brand block, top right */
  .brand { position: absolute; left: 590px; top: 42px; width: 330px; }
  .brand-disc {
    display: block; width: 120px; height: 120px; border-radius: 50%;
    background: var(--brand-light); margin-left: 36px;
  }
  .brand-name {
    margin-top: 16px; font-size: 34px; font-weight: 600; letter-spacing: 0.5px;
    color: var(--brand-light); line-height: 1;
  }
  .brand-rule { margin-top: 8px; height: 3px; width: 300px; background: var(--brand-light); }
  .brand-tagline {
    margin-top: 6px; font-family: "Tinos", "Times New Roman", serif; font-style: italic;
    font-size: 19px; color: var(--ink); padding-left: 28px;
  }

  /* Office contact, right */
  .office-contact { position: absolute; left: 640px; top: 296px; list-style: none; }
  .office-contact li { display: flex; align-items: flex-start; gap: 16px; font-size: 21px; line-height: 1.35; margin-bottom: 6px; letter-spacing: 0.5px; }
  .office-contact svg { flex: none; width: 24px; height: 24px; margin-top: 3px; fill: var(--ink); }

  /* Holder, left */
  .holder { position: absolute; left: 72px; top: 300px; }
  .holder-name { font-size: 40px; font-weight: 400; letter-spacing: 1.5px; line-height: 1; }
  .holder-rule { margin-top: 10px; height: 3px; width: 300px; background: var(--ink); }
  .holder-title { margin-top: 8px; font-size: 22px; letter-spacing: 2px; }

  .personal-contact { position: absolute; left: 72px; top: 410px; list-style: none; }
  .personal-contact li { display: flex; align-items: center; gap: 22px; font-size: 24px; line-height: 1; margin-bottom: 18px; letter-spacing: 0.5px; }
  .personal-contact svg { flex: none; width: 30px; height: 30px; fill: none; stroke: var(--ink); stroke-width: 2; }
</style>
</head>
<body>
  <article class="business-card">
    <header class="brand">
      <span class="brand-disc" aria-hidden="true"></span>
      <div class="brand-name">LIMBWELL INC.</div>
      <div class="brand-rule"></div>
      <div class="brand-tagline">Prosthetic &amp; Orthotic Services</div>
    </header>

    <ul class="office-contact">
      <li>
        <svg viewBox="0 0 24 24" aria-label="Phone"><path d="M6.6 10.8a15 15 0 0 0 6.6 6.6l2.2-2.2c.3-.3.7-.4 1-.2 1.1.4 2.3.6 3.6.6.6 0 1 .4 1 1V20c0 .6-.4 1-1 1A17 17 0 0 1 3 4c0-.6.4-1 1-1h3.5c.6 0 1 .4 1 1 0 1.3.2 2.5.6 3.6.1.3 0 .7-.2 1z"/></svg>
        <span>555 .310 .4820</span>
      </li>
      <li>
        <svg viewBox="0 0 24 24" aria-label="Fax"><path d="M7 2h10v5H7zM4 8h16a2 2 0 0 1 2 2v7h-4v5H6v-5H2v-7a2 2 0 0 1 2-2zm4 9v3h8v-3z"/></svg>
        <span>555 .310 .4821</span>
      </li>
      <li>
        <svg viewBox="0 0 24 24" aria-label="Address"><path d="M12 3l10 9h-3v9h-5v-6h-4v6H5v-9H2z"/></svg>
        <span>260 W.14th St.<br>Fairview,NY 10990</span>
      </li>
    </ul>

    <section class="holder">
      <h1 class="holder-name">Miriam Ostrander</h1>
      <div class="holder-rule"></div>
      <p class="holder-title">CO LPO</p>
    </section>

    <ul class="personal-contact">
      <li>
        <svg viewBox="0 0 30 30" aria-label="Mobile"><rect x="9" y="3" width="12" height="24" rx="2"/><line x1="13" y1="23" x2="17" y2="23"/></svg>
        <span>555 .204 .7731</span>
      </li>
      <li>
        <svg viewBox="0 0 30 30" aria-label="Email"><rect x="3" y="7" width="24" height="16"/><polyline points="3,7 15,17 27,7"/></svg>
        <span>mostrander@limbwellinc.com</span>
      </li>
      <li>
        <svg viewBox="0 0 30 30" aria-label="Website"><rect x="6" y="4" width="9" height="13" rx="4"/><rect x="15" y="13" width="9" height="13" rx="4"/></svg>
        <span>www.limbwellinc.com</span>
      </li>
    </ul>
  </article>
</body>
</html>
```